new KVR one page flyer

We need a 1 page A4 size flyer (need it asap please) that describes on 1 page with art work and using photos the services we provide. I have included some examples of old previous flyers from our other (seperate divisions of the business) I have named a photo called (photo for top of design) however you do your design this photo needs to be the star of the page by either having it at the top or bottom of the page please and we usually like this photo to be in greyscale colour.
we do like greyscale designs but are open to see what you come up with as a whole page of grey white and black might not suit.

Needs to list the following

Services include:
Over size loads / Hot Shot Loads
Heavy Vehicle Recovery services
Potable Water Deliveries
Road Building / Maintenance
Earthworks
Sand & Metal Supply & Cartage
Road Train Tippers
Road Train Tankers
Road Train Flat Tops
Drop Deck Trailers
Mine site accredited equipment & Operators.

We offer a large rage of services not listed so call us today for a personalised quote to suit your needs.

To go on the bottom of the page our contact details are

KVR Pty Ltd
Depot: Lot 514, Banksia Flats Track Coober Pedy
Mobile: 047 216 9381
email: darren@kestrelvaleroadworks.com.au

Target Market(s)

new clients

Colors

Designer to choose colors to be used in the design.

Requirements
Must have
• our services listed
Nice to have
• stand out designs

```html
<!DOCTYPE html>
<html lang="en">
<head>
<meta charset="utf-8">
<title>KVR Pty Ltd – Services Flyer</title>
<link rel="stylesheet" href="https://fonts.googleapis.com/css2?family=Fira+Sans+Condensed:ital,wght@0,600;0,700;0,800;1,600&family=Michroma&family=Roboto:wght@400;500;700&display=swap">
<style>
  :root {
    --orange: #f9a51b;
    --black: #1b1b1b;
    --charcoal: #2a2a2a;
    --light: #eeeeee;
    --white: #ffffff;
    --silver: #cfcfcf;
    --stage: #e4e4e4;
    --head: "Michroma", sans-serif;
    --list: "Fira Sans Condensed", sans-serif;
    --body: "Roboto", sans-serif;
  }
  * { box-sizing: border-box; margin: 0; padding: 0; }
  html, body { width: 1200px; height: 800px; overflow: hidden; background: var(--stage); }

  .flyer {
    position: absolute; left: 333px; top: 18px;
    width: 417px; height: 596px;
    transform: scale(1.28); transform-origin: 0 0;
    background: var(--white); overflow: hidden;
    box-shadow: 0 2px 6px rgba(0,0,0,.18);
  }
  .flyer > * { position: absolute; }

  .photo-top {
    left: 0; top: 0; width: 417px; height: 228px;
    background: linear-gradient(160deg, #d8d8d8 0%, #9a9a9a 35%, #4a4a4a 62%, #8c8c8c 85%, #b5b5b5 100%);
  }
  .photo-side {
    left: 0; top: 228px; width: 417px; height: 190px;
    clip-path: polygon(262px 0, 417px 0, 417px 190px, 214px 190px);
    background: linear-gradient(150deg, #f2f2f2 0%, #b8b8b8 40%, #3c3c3c 70%, #9c9c9c 100%);
  }
  .shapes { left: 0; top: 0; width: 417px; height: 596px; }

  .brand {
    left: 30px; top: 4px;
    font: 800 34px/1 var(--list); letter-spacing: 2px; color: var(--silver);
  }

  .contact { left: 252px; top: 8px; width: 160px; }
  .contact-label { display: flex; align-items: center; gap: 6px; font: 700 12.5px/1 var(--body); color: var(--white); padding-left: 22px; }
  .contact-phone { font: 700 19.5px/1 var(--body); color: var(--black); margin-top: 6px; padding-left: 14px; }

  .company-title {
    right: 15px; top: 113px; text-align: right;
    font: 400 19px/1.08 var(--head); color: var(--white); letter-spacing: .5px;
  }
  .title-rule { left: 262px; top: 161px; width: 141px; height: 3px; background: var(--orange); }
  .tagline {
    right: 15px; top: 170px; width: 200px; text-align: right;
    font: 400 12px/1.2 var(--body); color: var(--white);
  }

  .service-list { list-style: none; left: 14px; }
  .service-list li { display: flex; align-items: flex-start; gap: 8px; font-family: var(--list); font-style: italic; font-weight: 600; }
  .service-list .tick { flex: 0 0 15px; width: 15px; height: 15px; margin-top: 2px; }

  .list-orange { top: 236px; }
  .list-orange li { font-size: 15px; line-height: 19px; color: var(--white); margin-bottom: 8px; }
  .list-orange .tick circle { fill: var(--black); }
  .list-orange .tick path { stroke: var(--white); }

  .list-black { top: 333px; }
  .list-black li { font-size: 15px; line-height: 19px; color: var(--white); margin-bottom: 6px; }
  .list-black .tick circle { fill: var(--white); }
  .list-black .tick path { stroke: var(--black); }

  .list-light { top: 428px; }
  .list-light li { font-size: 13.5px; line-height: 13px; color: var(--black); margin-bottom: 9px; }
  .list-light .tick circle { fill: var(--orange); }
  .list-light .tick path { stroke: var(--white); }

  .offer {
    left: 216px; top: 434px; width: 196px; text-align: center;
    font: 700 12px/1.2 var(--body); color: var(--white);
  }

  .email { left: 14px; top: 541px; display: flex; align-items: center; gap: 8px; font: 400 10.5px/1 var(--body); color: var(--orange); }
  .depot { left: 234px; top: 522px; display: flex; gap: 8px; color: var(--white); }
  .depot .pin { margin-top: 14px; }
  .depot-name { font: 700 12px/1 var(--body); margin-bottom: 6px; }
  .depot-address { font: 400 8.5px/1.3 var(--body); }
</style>
</head>
<body>
<main class="flyer">

  <div class="photo-top" role="img" aria-label="Greyscale photo of a road train tipper truck on a dirt track in the outback"></div>
  <div class="photo-side" role="img" aria-label="Greyscale photo of a prime mover truck parked in a yard"></div>

  <svg class="shapes" viewBox="0 0 417 596" aria-hidden="true">
    <polygon points="0,0 232,0 208,45 0,45" fill="var(--black)"/>
    <polygon points="214,40 238,12 238,40" fill="var(--black)"/>
    <rect x="238" y="0" width="179" height="65" fill="var(--orange)"/>
    <polygon points="238,96 417,96 417,228 196,228" fill="rgba(30,30,30,.72)"/>
    <polygon points="0,228 250,228 226,322 0,322" fill="var(--orange)"/>
    <polygon points="250,228 264,228 216,418 202,418" fill="var(--black)"/>
    <polygon points="0,322 226,322 201,422 0,422" fill="var(--black)"/>
    <polygon points="0,422 210,422 186,522 0,522" fill="var(--light)"/>
    <polygon points="220,418 417,418 417,518 195,518" fill="var(--orange)"/>
    <polygon points="196,566 417,566 417,596 186,596" fill="var(--orange)"/>
    <polygon points="0,528 222,528 212,566 0,566" fill="var(--black)"/>
    <polygon points="224,514 417,514 417,566 211,566" fill="var(--black)"/>
  </svg>

  <div class="brand">KVR</div>

  <div class="contact">
    <div class="contact-label">
      <svg width="22" height="18" viewBox="0 0 22 18" aria-hidden="true">
        <rect x="1" y="1" width="14" height="10" rx="2" fill="none" stroke="#fff" stroke-width="1.6"/>
        <path d="M4 11 l0 4 l4 -4" fill="none" stroke="#fff" stroke-width="1.6"/>
        <rect x="8" y="6" width="13" height="9" rx="2" fill="var(--orange)" stroke="#fff" stroke-width="1.6"/>
        <circle cx="11.5" cy="10.5" r="1" fill="#fff"/><circle cx="14.5" cy="10.5" r="1" fill="#fff"/><circle cx="17.5" cy="10.5" r="1" fill="#fff"/>
      </svg>
      CONTACT US:
    </div>
    <div class="contact-phone">047 216 9381</div>
  </div>

  <h1 class="company-title">KESTREL VALE<br>ROADWORKS</h1>
  <div class="title-rule"></div>
  <p class="tagline">Providing services to our customers in some of the most remote locations in Australia</p>

  <ul class="service-list list-orange">
    <li><svg class="tick" viewBox="0 0 16 16"><circle cx="8" cy="8" r="8"/><path d="M4.5 8.3 l2.3 2.3 l4.7 -5" fill="none" stroke-width="1.8"/></svg>Over size loads / Hot Shot Loads</li>
    <li><svg class="tick" viewBox="0 0 16 16"><circle cx="8" cy="8" r="8"/><path d="M4.5 8.3 l2.3 2.3 l4.7 -5" fill="none" stroke-width="1.8"/></svg>Heavy Vehicle Recovery services</li>
    <li><svg class="tick" viewBox="0 0 16 16"><circle cx="8" cy="8" r="8"/><path d="M4.5 8.3 l2.3 2.3 l4.7 -5" fill="none" stroke-width="1.8"/></svg>Potable Water Deliveries</li>
  </ul>

  <ul class="service-list list-black">
    <li><svg class="tick" viewBox="0 0 16 16"><circle cx="8" cy="8" r="8"/><path d="M4.5 8.3 l2.3 2.3 l4.7 -5" fill="none" stroke-width="1.8"/></svg>Road Building / Maintenance</li>
    <li><svg class="tick" viewBox="0 0 16 16"><circle cx="8" cy="8" r="8"/><path d="M4.5 8.3 l2.3 2.3 l4.7 -5" fill="none" stroke-width="1.8"/></svg>Sand &amp; Metal Supply &amp; Cartage</li>
    <li><svg class="tick" viewBox="0 0 16 16"><circle cx="8" cy="8" r="8"/><path d="M4.5 8.3 l2.3 2.3 l4.7 -5" fill="none" stroke-width="1.8"/></svg>Drop Deck Trailers</li>
  </ul>

  <ul class="service-list list-light">
    <li><svg class="tick" viewBox="0 0 16 16"><circle cx="8" cy="8" r="8"/><path d="M4.5 8.3 l2.3 2.3 l4.7 -5" fill="none" stroke-width="1.8"/></svg><span>Road Train Tippers, Tankers<br>and Fat Tops</span></li>
    <li><svg class="tick" viewBox="0 0 16 16"><circle cx="8" cy="8" r="8"/><path d="M4.5 8.3 l2.3 2.3 l4.7 -5" fill="none" stroke-width="1.8"/></svg><span>Mine site accredited<br>equipment &amp; Operators.</span></li>
    <li><svg class="tick" viewBox="0 0 16 16"><circle cx="8" cy="8" r="8"/><path d="M4.5 8.3 l2.3 2.3 l4.7 -5" fill="none" stroke-width="1.8"/></svg>Earthworks</li>
  </ul>

  <p class="offer">We offer a large rage of services not listed so call us today for a personalised quote to suit your needs.</p>

  <div class="email">
    <svg width="18" height="12" viewBox="0 0 18 12" aria-hidden="true">
      <rect x="1" y="1" width="16" height="10" fill="none" stroke="var(--orange)" stroke-width="1.6"/>
      <path d="M1 1 l8 6 l8 -6" fill="none" stroke="var(--orange)" stroke-width="1.6"/>
    </svg>
    darren@kestrelvaleroadworks.com.au
  </div>

  <div class="depot">
    <svg class="pin" width="12" height="16" viewBox="0 0 12 16" aria-hidden="true">
      <path d="M6 0 a6 6 0 0 1 6 6 c0 4 -6 10 -6 10 s-6 -6 -6 -10 a6 6 0 0 1 6 -6z" fill="var(--orange)"/>
      <circle cx="6" cy="6" r="2.2" fill="var(--black)"/>
    </svg>
    <div>
      <div class="depot-name">KVR Pty Ltd</div>
      <div class="depot-address">Depot: Lot 514,<br>Banksia Flats Track Coober Pedy</div>
    </div>
  </div>

</main>
</body>
</html>
```